Blueprint and Beyond - Invitation

Need a three fold, 8.5 X 11 invitation that will be direct mail for a seminar. We develop properties for churches in the United States. Final design should communicate a compelling reason for church leaders to attend the "Blueprint and Beyond" seminar. To be clear, the folded and complete invitation is 8.5" X 11" so there are a total of 6 panels measuring 8.5" X 11". Thanks and have fun.
Updates

Went on vacation/holiday

Target Market(s)

Young start up churches, highly energetic, not traditional at all.

Colors
0054AA
0677BA
7BADD7
CADEEF
E8F1F8
FFF300
FFF600
FEFA6F
FFFEC7
FFFEE8
FFC000
F8CF3A
FAE287
FDF2CF
FEFAEE
EB3D1F
EC4F4E
F09395
F8D3D4
FCEDEE

Requirements
Must have
• See the mock up brochure that I made up. It has all the info I need.
Nice to have
• Open space. Mock up is much too busy looking. Gives me a headache!
Should not have
• Nothing traditional church looking.

```html
<!DOCTYPE html>
<html lang="en">
<head>
<meta charset="utf-8">
<title>Blueprint and Beyond – Seminar Invitation</title>
<link href="https://fonts.googleapis.com/css2?family=Roboto+Condensed:wght@300;400;700&family=UnifrakturMaguntia&display=swap" rel="stylesheet">
<style>
:root{
  --navy:#1f3d6b;
  --yellow:#f8c23a;
  --cream:#fdecc4;
  --red:#e8441f;
  --red-soft:#ec4f4e;
  --orange:#f26b2a;
  --white:#ffffff;
  --stage:#c7c7c7;
  --ink:#1c2f52;
}
*{box-sizing:border-box;margin:0;padding:0}
html,body{width:1200px;height:2362px;overflow:hidden}
body{background:var(--stage);font-family:"Roboto Condensed",Arial,sans-serif;color:var(--white);position:relative}
.spread{position:absolute;box-shadow:0 6px 14px rgba(0,0,0,.35);overflow:hidden}
.spread--outside{left:225px;top:120px;width:765px;height:592px;background:var(--white)}
.spread--inside{left:230px;top:1688px;width:753px;height:582px;background:var(--cream)}
.panel{position:absolute;top:0;height:100%;overflow:hidden}
.abs{position:absolute}
.photo{position:absolute}
.body-text{font-family:"Roboto Condensed",Arial,sans-serif;font-weight:300;font-size:11px;line-height:1.08}

/* outside panel 1 */
.story{left:0;width:255px;background:var(--navy)}
.story .intro-photo{left:0;top:0;width:115px;height:135px;background:linear-gradient(160deg,#e9e4dc,#a77a58 60%,#6b4a33)}
.story .intro{left:116px;top:18px;width:132px}
.story .intro-tail{left:16px;top:140px;width:232px}
.story .growth{left:16px;top:176px;width:232px}
.red-tag{position:absolute;left:0;background:var(--red);color:var(--white);font-weight:700;font-size:16px;padding-left:16px;width:178px;height:20px;line-height:20px}
.story .bad-tag{top:224px}
.story .bad{left:16px;top:248px;width:232px}
.story .good-tag{top:367px}
.story .good{left:16px;top:390px;width:232px}
.verse{position:absolute;left:0;top:417px;width:255px;height:50px;background:var(--yellow);color:#c8241a;font-family:"UnifrakturMaguntia",serif;font-size:14.5px;line-height:1.05;text-align:center;padding:5px 10px 0}
.verse cite{position:absolute;right:14px;bottom:2px;font-family:"Roboto Condensed",sans-serif;font-style:normal;font-size:8px;color:var(--ink)}
.story .building-photo{left:0;top:467px;width:255px;height:125px;background:linear-gradient(#3a7bd5 0,#9cc6ee 35%,#c9a98a 55%,#8f7a63 75%,#6d6f66)}

/* outside panel 2 */
.benefits{left:255px;width:255px;background:var(--white)}
.yellow-head{position:absolute;left:0;width:255px;background:var(--yellow);color:var(--white);font-weight:700;font-size:17px;line-height:.98;padding-left:14px}
.benefits .help-head{top:0;height:52px;padding-top:17px}
.cream-list{position:absolute;left:0;width:255px;background:var(--cream);color:var(--ink);list-style:none;padding:2px 16px 4px 36px;font-weight:300;font-size:10px;line-height:1.13}
.cream-list li{position:relative}
.cream-list li::before{content:"";position:absolute;left:-9px;top:4px;width:4px;height:4px;border-radius:50%;background:var(--red)}
.benefits .help-list{top:52px;height:111px}
.benefits .topics-head{top:163px;height:33px}
.benefits .topics-list{top:196px;height:180px;line-height:1.38}
.contact-card{position:absolute;left:0;top:376px;width:255px;height:75px;background:var(--navy)}
.contact-card .head-photo{left:20px;top:8px;width:62px;height:62px;background:linear-gradient(#7d8a6c,#d9b79b 55%,#5d6b7c)}
.contact-card .name{left:86px;top:12px;font-size:11.5px;line-height:1.05;font-weight:700}
.contact-card .name span{font-weight:300;display:block}
.contact-card .register{left:86px;top:56px;font-size:11px;font-weight:300}
.seat-note{position:absolute;left:188px;top:6px;width:56px;height:42px;background:var(--yellow);color:var(--ink);font-weight:700;font-size:10px;line-height:.95;text-align:center;padding-top:6px;transform:rotate(-8deg)}

/* outside panel 3 – cover */
.cover{left:510px;width:255px;background:var(--white)}
.cover .top{left:0;top:0;width:255px;height:340px;background:var(--navy);border-bottom-left-radius:70px}
.brand{position:absolute;left:40px;top:16px;display:flex;align-items:center;gap:8px;color:var(--white)}
.brand .dot{width:12px;height:12px;border-radius:50%;background:var(--white)}
.brand .name{font-size:27px;line-height:1;letter-spacing:1px;font-weight:400}
.brand .tag{position:absolute;left:64px;top:31px;font-size:13px;letter-spacing:1px;white-space:nowrap;font-weight:400}
.cover .lodge-photo{left:0;top:86px;width:255px;height:104px;background:linear-gradient(#8fb4d8 0,#c8dbe8 30%,#7a5b45 55%,#3e4a3a 80%,#5a5c58)}
.cover .pastor{left:60px;top:194px;color:var(--yellow);font-weight:700;font-size:38px;line-height:1}
.cover .lead{left:32px;top:234px;font-weight:700;color:var(--white);line-height:.9}
.lead .big{font-size:33px}
.lead .small{font-size:16px;color:var(--yellow);font-weight:400}
.lead .l1,.lead .l2,.lead .l3{display:block}
.lead .l2{padding-left:40px}
.lead .l3{padding-left:60px}
.cover .attend{left:14px;top:346px;width:236px;color:var(--navy);line-height:.95}
.attend .pre{font-size:21px;font-weight:300;display:block;text-align:center}
.attend .title{font-size:24px;font-weight:700;display:block;margin-top:2px;text-align:center;white-space:nowrap}
.attend .seminar{font-size:36px;font-weight:700;display:block;padding-left:6px}
.price{position:absolute;left:182px;top:392px;width:56px;height:56px;border-radius:50%;background:var(--red);border:2px dashed var(--yellow);color:var(--yellow);text-align:center;font-size:22px;font-weight:700;line-height:52px;transform:rotate(-12deg)}
.cover .learn{left:0;top:446px;width:255px;text-align:center;color:var(--ink);font-weight:300;font-size:10.5px;line-height:1.08}
.learn strong{font-weight:700;font-size:14px;color:var(--navy)}
.cover .dates{left:0;top:498px;width:255px;height:38px;background:var(--yellow);border-radius:16px 16px 0 0;color:var(--navy);text-align:center;padding-top:4px;font-size:14px;font-weight:300;line-height:1.05}
.dates b{font-weight:700}
.dates .cities{display:block;font-size:10.5px;margin-top:3px}
.cover .phone{left:0;top:536px;width:255px;height:26px;color:var(--navy);text-align:center;font-weight:700;font-size:22px;line-height:26px}
.cover .web{left:0;top:562px;width:255px;height:30px;background:var(--navy);color:var(--white);text-align:center;font-weight:700;font-size:21px;line-height:30px}

/* inside */
.hall-photo{left:0;top:0;width:753px;height:228px;background:linear-gradient(#6b5848 0,#3c3a38 35%,#2e5a45 45%,#9a7a5e 70%,#c08a5c)}
.inside-panel{top:228px;height:354px}
.overwhelmed{left:0;width:251px;background:var(--cream)}
.speaker{left:251px;width:251px;background:var(--navy)}
.attendees{left:502px;width:251px;background:var(--cream)}
.navy-head{position:absolute;color:var(--navy);font-weight:700;font-size:15.5px;line-height:1}
.ink{color:var(--ink)}
.orange-band{position:absolute;left:0;width:251px;background:linear-gradient(90deg,var(--orange),var(--red) 55%,#f7a23a);color:var(--white);font-weight:700;text-align:center}
.overwhelmed .h{left:16px;top:10px}
.overwhelmed .t1{left:16px;top:28px;width:225px}
.overwhelmed .q{left:40px;top:56px}
.overwhelmed .band{top:92px;height:36px;font-size:11px;line-height:1;padding-top:7px}
.overwhelmed .t2{left:16px;top:132px;width:225px}
.overwhelmed .come{left:16px;top:185px;color:var(--red);font-weight:700;font-size:15px}
.overwhelmed .t3{left:16px;top:204px;width:145px}
.badge{position:absolute;z-index:2;border-radius:50%;background:var(--red);border:2px dashed var(--yellow);color:var(--white);text-align:center;font-weight:700;line-height:1;transform:rotate(-22deg);display:flex;align-items:center;justify-content:center}
.overwhelmed .badge{left:160px;top:218px;width:78px;height:78px;font-size:9.5px}
.overwhelmed .church-photo{left:0;top:262px;width:251px;height:92px;background:linear-gradient(#e9dccb,#b99a7c 50%,#8a7260)}

.speaker-copy{position:absolute;left:12px;top:8px;width:228px;color:var(--white)}
.speaker-copy .portrait{float:left;width:86px;height:96px;margin:0 6px 4px 0;border-radius:30px;background:radial-gradient(#d9b79b,#6a7b99 75%,var(--navy))}
.speaker-copy h2{font-weight:700;font-size:15.5px;line-height:1.1;margin-bottom:2px}
.speaker-copy p{font-size:10.5px}
.speaker-copy p + p{margin-top:6px}
.speaker-copy .badge-space{float:right;width:62px;height:64px}
.speaker .badge{left:186px;top:190px;width:60px;height:60px;font-size:9.5px;color:var(--yellow)}
.speaker .campus-photo{left:0;top:276px;width:251px;height:78px;background:linear-gradient(#bcd3ea,#e0e6ea 30%,#9aa087 60%,#6a7652)}

.attendees .h1{left:16px;top:10px;width:225px}
.attendees .t1{left:16px;top:46px;width:225px}
.attendees .h2{left:16px;top:92px}
.attendees .t2{left:16px;top:110px;width:225px}
.attendees .band{top:166px;height:34px;font-size:15px;line-height:34px;background:linear-gradient(90deg,var(--red-soft),var(--orange) 60%,#f7a23a)}
.attendees .worship-photo{left:0;top:200px;width:251px;height:154px;background:linear-gradient(#1c1430,#7a2e8c 35%,#3a1f4a 65%,#2a1a14)}
</style>
</head>
<body>

<section class="spread spread--outside" aria-label="Invitation outside spread">
  <div class="panel story">
    <div class="photo intro-photo" role="img" aria-label="Portrait photo of a smiling pastor couple"></div>
    <p class="abs body-text intro">I remember sitting at my desk back in 2001, wondering what am I going to do? Wishing that there was someone I could call that had the knowledge and experience to guide me in the right direction. That is when a seminar invitation</p>
    <p class="abs body-text intro-tail">showed up on my desk and I soon met Dan Ashford.</p>
    <p class="abs body-text growth">Since then, The Cedar Fellowship has gone through numerous building programs, grown to over 5,000 in attendance and grown into a thriving ministry with a high global impact.</p>
    <div class="red-tag bad-tag">Here's the bad news:</div>
    <p class="abs body-text bad">The average tenure of a pastor after a significant building project is twenty-two months. Over half of the churches in the U.S. have a set of plans (stuck behind the pastor's door) that will never be built. To top it off, construction is the second most litigated industry in the U.S. behind medical. Some pastors will deal with these statistics by never building. Some will forge ahead alone and often become one of these statistics.</p>
    <div class="red-tag good-tag">The good news is</div>
    <p class="abs body-text good">that others will seek out those who have built to gain counsel and wisdom.</p>
    <blockquote class="verse">“Plans fail for lack of counsel, but with many advisors they succeed”<cite>Proverbs 15:22”</cite></blockquote>
    <div class="photo building-photo" role="img" aria-label="Photo of a modern two-storey church building with palm trees"></div>
  </div>

  <div class="panel benefits">
    <h2 class="yellow-head help-head">We help Pastors and<br>church leaders to:</h2>
    <ul class="cream-list help-list">
      <li>Develop state of the art facilities that are functional &amp; affordable</li>
      <li>Reduce the stress and distractions of a building program</li>
      <li>Avoid the pitfalls of typical building projects</li>
      <li>Eliminate those unexpected surprises</li>
      <li>Maximize Ministry Momentum by eliminating growth barriers.</li>
    </ul>
    <h2 class="yellow-head topics-head">The seminar teaches a variety<br>of topics including:</h2>
    <ul class="cream-list topics-list">
      <li>10-Steps to Your New Facility</li>
      <li>Creative Land Acquisition</li>
      <li>Funding Your Building Program</li>
      <li>What Type of Building is Right for You</li>
      <li>Creative Church Designs</li>
      <li>Time and Talent Surveys</li>
      <li>Meet Your Development Team</li>
      <li>Debt Free Development</li>
      <li>Understanding the Permit Process</li>
      <li>Dealing with Nasty Neighbors</li>
      <li>Developing a Communication Plan</li>
      <li>Master Planning Your Campus</li>
    </ul>
    <div class="contact-card">
      <div class="photo head-photo" role="img" aria-label="Headshot of the seminar speaker"></div>
      <p class="abs name">Daniel R. Ashford<span>America's #1<br>Church Developer</span></p>
      <p class="abs register">Contact Dan Ashford to register.</p>
      <div class="seat-note">Seating<br>is<br>limited</div>
    </div>
  </div>

  <div class="panel cover">
    <div class="abs top"></div>
    <div class="brand"><span class="dot"></span><span class="name">KEYSTONE</span><span class="tag">facility solutions</span></div>
    <div class="photo lodge-photo" role="img" aria-label="Photo of a timber and stone church lodge entrance"></div>
    <p class="abs pastor">PASTOR!</p>
    <p class="abs lead"><span class="l1"><span class="big">Lead</span></span><span class="l2"><span class="small">your</span></span><span class="l2"><span class="big">church</span> <span class="small">with</span></span><span class="l3"><span class="big">confidence</span></span></p>
    <h1 class="abs attend"><span class="pre">Attend the</span><span class="title">Blueprint and Beyond</span><span class="seminar">Seminar</span></h1>
    <div class="price">$29</div>
    <p class="abs learn">Learn how to<br>DESIGN, FINANCE and BUILD<br>the most creative, functional and affordable<br><strong>church facilities in America!</strong></p>
    <p class="abs dates">Coming to the <b>Bay Area, March 4-7</b><span class="cities">Santa Rosa | Walnut Creek | San Jose | San Mateo</span></p>
    <p class="abs phone">555-014-2870</p>
    <p class="abs web">Ashfordbuilds.com</p>
  </div>
</section>

<section class="spread spread--inside" aria-label="Invitation inside spread">
  <div class="photo hall-photo" role="img" aria-label="Photo of a packed seminar hall with a speaker on stage and a projected chart"></div>

  <div class="panel inside-panel overwhelmed">
    <h2 class="navy-head h">FEELING A BIT OVERWHELMED?</h2>
    <p class="abs body-text ink t1">We get it. God is growing your ministry, but your current facilities cannot sustain it.</p>
    <p class="abs body-text ink q">Where do you start?<br>Who do you call?<br>What are you going to do?</p>
    <div class="orange-band band">ASKING GOD FOR<br>GUIDANCE AND DIRECTION?</div>
    <p class="abs body-text ink t2">You need a Kingdom focused ally with over forty years experience developing hundreds of state-of-the-art, Christian church facilities all across America.</p>
    <p class="abs come">That is where we come in!</p>
    <p class="abs body-text ink t3">Discover the possibilities you may not even know exist and then seize your God-given potential!</p>
    <div class="badge">Pastors,<br>elders,<br>church staff<br>and<br>volunteers<br>are all<br>invited!</div>
    <div class="photo church-photo" role="img" aria-label="Photo of a brick church building exterior"></div>
  </div>

  <div class="panel inside-panel speaker">
    <div class="speaker-copy">
      <div class="portrait" role="img" aria-label="Portrait of the seminar speaker"></div>
      <h2>ABOUT OUR SPEAKER</h2>
      <p class="body-text">Dan Ashford, founder of Keystone Facility Solutions, is America's top developer of Christian church facilities. Beginning in 1980, Dan has used his wisdom and experience to help ministries like yours to overcome the challenges to their facility needs and growth barriers. Dan's unique understanding of ministry needs make him a trusted partner for churches that need functional and affordable facilities that are designed to grow with them.</p>
      <div class="badge-space"></div>
      <p class="body-text">If you are looking for expert guidance and direction in the design, finance and construction of your new, expanded or remodeled facilities, then this is your opportunity to learn from the nations leading expert on church design, finance and construction.</p>
    </div>
    <div class="badge">Learn<br>from the<br>experience<br>of others!</div>
    <div class="photo campus-photo" role="img" aria-label="Photo of a church campus with a green roof and lawn"></div>
  </div>

  <div class="panel inside-panel attendees">
    <h2 class="navy-head h1">Maximize your ministry potential for greater Kingdom impact!</h2>
    <p class="abs body-text ink t1">Cast a clear and compelling vision for the future and build a road map connecting your current reality to your future potential!</p>
    <h2 class="navy-head h2">WHO SHOULD ATTEND?</h2>
    <p class="abs body-text ink t2">Whether you are looking to relocate, expand, remodel or build new, this seminar will equip you with the tools and confidence you need. Pastors, elders, church staff and volunteers are all invited!</p>
    <div class="orange-band band">BRING YOUR ENTIRE TEAM!</div>
    <div class="photo worship-photo" role="img" aria-label="Photo of a worship service with purple stage lights and a crowd"></div>
  </div>
</section>

</body>
</html>
```